Marlow Hire Business Card for recruitment company

We are looking for a Business Card Design that incorporates our personal details and our busines name and logo. We are a specialized search consultancy that recruit Property and Construction professionals.
We would like a business card that stands out and is appealing to the Construction and Property industry as well.

Target Market(s)

people in the construction and property industry

Contact Information for Business Card

Business Name and logo

Font styles to use
Serif

Colors
0094D4
00A9DD
6FCCEA
C7EBF8
E9F6FB

Requirements
Must have
• Business name and logo as well as contact details
Should not have
• No photos of us please

```html
<!DOCTYPE html>
<html lang="en">
<head>
<meta charset="utf-8">
<title>Marlow Hire — Business Card</title>
<link rel="stylesheet" href="https://fonts.googleapis.com/css2?family=Source+Sans+3:wght@300;400;700&display=swap">
<style>
  :root {
    --navy: #0a3c52;
    --navy-ink: #0d4259;
    --white: #ffffff;
    --mark-tint: #e4ecef;
    --backdrop: #e8e6e3;
  }
  * { box-sizing: border-box; margin: 0; padding: 0; }
  html, body {
    width: 1083px;
    height: 1200px;
    overflow: hidden;
    background: var(--backdrop);
    font-family: "Source Sans 3", "Source Sans Pro", Arial, sans-serif;
  }
  .canvas { position: relative; width: 1083px; height: 1200px; }

  .card {
    position: absolute;
    left: 91px;
    width: 900px;
    height: 510px;
    overflow: hidden;
    box-shadow: 0 6px 18px rgba(0, 0, 0, 0.12);
  }
  .card--front { top: 58px; background: var(--white); }
  .card--back { top: 632px; background: var(--navy); }

  .wordmark {
    position: absolute;
    font-weight: 400;
    text-transform: uppercase;
    line-height: 1;
    white-space: nowrap;
  }
  .card--front .wordmark {
    left: 55px;
    top: 48px;
    font-size: 64px;
    letter-spacing: 0.06em;
    color: var(--navy);
  }
  .card--back .wordmark {
    left: 0;
    right: 0;
    top: 196px;
    text-align: center;
    font-size: 92px;
    letter-spacing: 0.08em;
    color: var(--white);
  }

  .brand-mark-area {
    position: absolute;
    left: 0;
    top: 126px;
    width: 320px;
    height: 297px;
    background: var(--mark-tint);
  }

  .contact {
    position: absolute;
    left: 455px;
    top: 184px;
    color: var(--navy-ink);
  }
  .contact__name {
    font-size: 26px;
    line-height: 32px;
    font-weight: 700;
    letter-spacing: 0.2em;
    text-transform: uppercase;
    margin-bottom: 12px;
  }
  .contact__line {
    font-size: 27px;
    font-weight: 300;
    line-height: 43px;
  }
  .contact__label { font-weight: 700; }

  .web-pill {
    position: absolute;
    height: 56px;
    border-radius: 28px;
    display: flex;
    align-items: center;
    justify-content: center;
    font-size: 27px;
    font-weight: 300;
  }
  .card--front .web-pill {
    left: 455px;
    top: 323px;
    width: 370px;
    background: var(--navy);
    color: var(--white);
  }
  .card--back .web-pill {
    left: 264px;
    top: 336px;
    width: 368px;
    background: var(--white);
    color: var(--navy);
  }

  .hours-band {
    position: absolute;
    left: 0;
    bottom: 0;
    width: 100%;
    height: 87px;
    background: var(--navy);
    color: var(--white);
    display: flex;
    align-items: center;
    justify-content: center;
    font-size: 28px;
    font-weight: 300;
  }
  .hours-band strong { font-weight: 700; margin-right: 8px; }
</style>
</head>
<body>
  <main class="canvas">
    <section class="card card--front" aria-label="Business card front">
      <h1 class="wordmark">Marlow Hire</h1>
      <div class="brand-mark-area" role="img" aria-label="Large brand symbol decoration"></div>
      <div class="contact">
        <p class="contact__name">Clara Benton</p>
        <p class="contact__line"><span class="contact__label">E:</span> clara@MarlowHire.nz</p>
        <p class="contact__line"><span class="contact__label">T:</span> +64 27 555 0142</p>
      </div>
      <p class="web-pill">www.MarlowHire.nz</p>
      <p class="hours-band"><strong>Monday - Friday:</strong> 8:00am - 6:00pm NZST</p>
    </section>

    <section class="card card--back" aria-label="Business card back">
      <h2 class="wordmark">Marlow Hire</h2>
      <p class="web-pill">www.MarlowHire.nz</p>
    </section>
  </main>
</body>
</html>
```